Denture Clinic needs a newspaper advertisement

We need a revamped newspaper advertisement for our denture clinic based in Tweed Heads, Australia. We are currently promoting a new product called FlexaLume which is a virtually non breakable, flexible denture. We have an ad the newspaper designed themselves but I feel the ad gets lost on the page and isn't effective. They have used our brand colours but apparently so does everyone else in the newspaper! We would like to see an ad that shows a quality, state of the art product but something that jumps out of the page and overrides the other ads nearby. We can't use colours that stimulate fear (like blood red) or anxiety being a dentist or black.

I have also attached a copy of the one-off full page ad we ran which shows more information about the product.

The ad size is 92mm high by 129mm wide.

Target Market(s)

95% of our patients are 65+ years old

Industry/Entity Type

Clinic

Requirements
Must have
• Must show the denture, our name, logo and details and state it is virtually unbreakable and flexible.
Should not have
• Colours that evoke fear, anxiety, trepidation.

```html
<!DOCTYPE html>
<html lang="en">
<head>
<meta charset="utf-8">
<title>Coastal Ridge Denture Clinic – FlexaLume Advertisement</title>
<link href="https://fonts.googleapis.com/css2?family=Arimo:wght@400;700&family=Oswald:wght@600;700&display=swap" rel="stylesheet">
<style>
  :root {
    --navy: #3a4f8c;
    --navy-deep: #1c2a5c;
    --ink: #111111;
    --magenta: #c2267e;
    --sky-top: #cfe6f1;
    --sky-mid: #e4f0f6;
    --panel: rgba(255,255,255,0.9);
    --white: #ffffff;
    --rule: #c9ccd3;
  }
  * { margin: 0; padding: 0; box-sizing: border-box; }
  html, body { width: 1200px; height: 1000px; overflow: hidden; background: var(--white); }
  body { font-family: "Arimo", Arial, sans-serif; color: var(--ink); position: relative; }

  .ad {
    position: absolute; left: 0; top: 72px; width: 1200px; height: 856px;
    background: linear-gradient(180deg, var(--sky-top) 0%, var(--sky-mid) 45%, #f4f8fa 75%, #e9eef2 100%);
    overflow: hidden;
  }
  .couple-photo {
    position: absolute; left: 0; top: 170px; width: 880px; height: 580px;
    background: radial-gradient(ellipse at 35% 45%, #e6d9d4 0%, #d8d2cc 30%, rgba(210,220,228,0.6) 60%, rgba(225,236,242,0) 80%);
  }

  .brand { position: absolute; left: 40px; top: 24px; display: flex; align-items: center; gap: 16px; }
  .brand-mark { width: 110px; height: 110px; border-radius: 50%; background: var(--navy); }
  .brand-name { font-weight: 700; color: var(--navy); font-size: 34px; line-height: 1.05; }

  .panel { position: absolute; background: var(--panel); }
  .panel-intro { left: 555px; top: 27px; width: 288px; height: 330px; padding: 22px 20px 0 24px; }
  .intro-text { font-size: 16.5px; line-height: 1.6; }
  .intro-text strong { color: var(--navy); }
  .benefits { list-style: none; margin-top: 26px; }
  .benefits li { position: relative; padding-left: 22px; font-weight: 700; font-size: 16px; line-height: 1.63; }
  .benefits svg { position: absolute; left: 0; top: 5px; }

  .panel-allergy { left: 876px; top: 27px; width: 288px; height: 450px; padding: 18px 14px 0 26px; }
  .allergy-text { font-weight: 700; font-size: 16px; line-height: 1.6; }
  .clasp-badge { position: absolute; left: 0px; top: 108px; width: 150px; height: 150px; }
  .denture-photo {
    position: absolute; left: 20px; top: 180px; width: 262px; height: 210px;
    background: radial-gradient(ellipse at 55% 50%, #e7b9c3 0%, #efd5da 45%, rgba(255,255,255,0) 75%);
  }
  .footnote { position: absolute; left: 896px; top: 442px; font-size: 12.5px; line-height: 1.55; width: 250px; }

  .headline {
    position: absolute; right: 42px; top: 540px; text-align: right;
    font-family: "Oswald", "Arial Narrow", sans-serif; font-weight: 700;
    font-size: 60px; line-height: 1.0; color: var(--navy);
    letter-spacing: 0.5px;
    text-shadow: 0 0 2px #fff, 0 0 4px #fff;
  }
  .headline .second { color: var(--navy-deep); }
  .tagline {
    position: absolute; right: 42px; top: 676px;
    font-family: "Oswald", "Arial Narrow", sans-serif; font-weight: 600;
    font-size: 33px; color: var(--white); letter-spacing: 0.3px;
    text-shadow: 1px 2px 4px rgba(0,0,0,0.55);
  }

  .footer {
    position: absolute; left: 0; bottom: 0; width: 1200px; height: 106px;
    background: var(--navy); border-top: 4px solid var(--rule);
    color: var(--white);
  }
  .footer-web { position: absolute; left: 38px; top: 18px; font-weight: 700; font-size: 30px; }
  .footer-address { position: absolute; left: 38px; top: 62px; font-size: 18px; font-weight: 700; letter-spacing: 0.6px; }
  .footer-phone {
    position: absolute; right: 46px; top: 12px;
    font-family: "Oswald", "Arial Narrow", sans-serif; font-weight: 600; font-size: 58px;
    text-shadow: 1px 2px 3px rgba(0,0,0,0.4);
  }
</style>
</head>
<body>
<main class="ad">
  <div class="couple-photo" role="img" aria-label="Photo of a smiling senior couple leaning on a railing, the man pointing towards the product"></div>

  <div class="brand">
    <div class="brand-mark"></div>
    <div class="brand-name">Coastal Ridge<br>Denture Clinic</div>
  </div>

  <section class="panel panel-intro">
    <p class="intro-text">Introducing <strong>FlexaLume by Meridian.</strong> The flexible, virtually unbreakable* denture injection system, using advanced dental prosthetic technology.</p>
    <ul class="benefits">
      <li><svg width="17" height="15" viewBox="0 0 17 15"><path d="M1 8 L6 13 L16 1" fill="none" stroke="#c2267e" stroke-width="3"/></svg>Undetectable in the Mouth</li>
      <li><svg width="17" height="15" viewBox="0 0 17 15"><path d="M1 8 L6 13 L16 1" fill="none" stroke="#c2267e" stroke-width="3"/></svg>Can be claimed through Private Health Funds and DVA</li>
      <li><svg width="17" height="15" viewBox="0 0 17 15"><path d="M1 8 L6 13 L16 1" fill="none" stroke="#c2267e" stroke-width="3"/></svg>Full or Partial Dentures</li>
      <li><svg width="17" height="15" viewBox="0 0 17 15"><path d="M1 8 L6 13 L16 1" fill="none" stroke="#c2267e" stroke-width="3"/></svg>Available in 10 Shades</li>
    </ul>
  </section>

  <section class="panel panel-allergy">
    <p class="allergy-text">And they’re suitable for patients with allergic reactions or other sensitivity problems too!</p>
    <div class="denture-photo" role="img" aria-label="Photo of a flexible partial denture with transparent pink clasps"></div>
    <svg class="clasp-badge" viewBox="0 0 150 150" aria-label="Transparent Clasps">
      <circle cx="75" cy="75" r="62" fill="none" stroke="#c2267e" stroke-width="14" stroke-dasharray="6 5"/>
      <circle cx="75" cy="75" r="62" fill="#c2267e"/>
      <g transform="rotate(-15 75 75)" fill="#fff" font-family="Arimo, Arial, sans-serif" font-weight="700" font-size="19" text-anchor="middle">
        <text x="75" y="70">Transparent</text>
        <text x="75" y="93">Clasps</text>
      </g>
    </svg>
  </section>

  <p class="footnote">*Please note ‘virtually unbreakable’ refers to the nylon base of the denture only.</p>

  <h1 class="headline">WANT COMFORTABLE, NEAR<br><span class="second">UNBREAKABLE DENTURES?</span></h1>
  <p class="tagline">CALL TO FIND SOMETHING TO SMILE ABOUT!</p>

  <footer class="footer">
    <div class="footer-web">www.coastalridgedentures.com.au</div>
    <div class="footer-address">Daniel Ashcombe AdvDipDP Dip DT - 12 Harbour Lane, Coral Bay</div>
    <div class="footer-phone">(07) 5550 1827</div>
  </footer>
</main>
</body>
</html>
```